Business Card design for new private practice opening

I need a business card design for my new private practice with my new logo uploaded as a file
On the front the logo
On the back: maybe a small logo somewhere?
Priv. Doz. DDr. Corinna Vestaluk
Fachärztin für Allgemein- & Viszeralchirurgie
Address: xxx
Tel: xxx
Mobil:xxx
Webseite:xxx
Email:xxx

Contact Information for Business Card

See project description above for details

Requirements
Nice to have
• I would like the colors of the logo incorporated into the business card

```html
<!DOCTYPE html>
<html lang="de">
<head>
<meta charset="utf-8">
<title>Velmora Chirurgie – Visitenkarte</title>
<link href="https://fonts.googleapis.com/css2?family=Montserrat:wght@400;500;600;700&display=swap" rel="stylesheet">
<style>
  :root {
    --page-bg: #e9e6e1;
    --teal: #2a9a94;
    --teal-dark: #146a66;
    --teal-light: #35a9a2;
    --grey-text: #6b6b6b;
    --dark-text: #4a4a4a;
    --card-white: #ffffff;
    --faint-teal: #dff0f0;
    --faint-ring: #ececec;
  }
  * { margin: 0; padding: 0; box-sizing: border-box; }
  html, body { width: 1200px; height: 900px; overflow: hidden; }
  body {
    background: var(--page-bg);
    font-family: "Montserrat", sans-serif;
    position: relative;
  }
  .card {
    position: absolute;
    width: 620px;
    height: 354px;
    border-radius: 30px;
    overflow: hidden;
    box-shadow: 0 10px 28px rgba(0,0,0,0.22);
  }

  /* Front card */
  .card-front {
    left: 110px; top: 50px;
    background: linear-gradient(160deg, #ffffff 40%, #ececec 100%);
  }
  .front-deco {
    position: absolute;
    right: -40px; top: -70px;
    width: 250px; height: 250px;
    border-radius: 50%;
    background: var(--faint-teal);
    border: 10px solid var(--faint-ring);
    opacity: 0.8;
  }
  .brand {
    display: flex; align-items: center; gap: 14px;
  }
  .brand-dot {
    width: 62px; height: 62px; border-radius: 50%;
    background: var(--teal);
    flex: none;
  }
  .brand-name {
    font-weight: 700;
    font-size: 27px;
    line-height: 1.02;
    letter-spacing: 1px;
    text-transform: uppercase;
    color: var(--grey-text);
  }
  .card-front .brand {
    position: absolute; left: 36px; top: 70px;
  }
  .front-rule {
    position: absolute; left: 36px; top: 160px;
    width: 270px; height: 1px; background: #bdbdbd;
  }
  .person {
    position: absolute; left: 36px; top: 172px;
  }
  .person-name {
    color: var(--teal);
    font-weight: 600;
    font-size: 18px;
  }
  .person-title {
    color: var(--dark-text);
    font-size: 12px;
    margin-top: 3px;
  }
  .contact-list {
    list-style: none;
    margin-top: 16px;
    font-size: 12.5px;
    color: var(--dark-text);
  }
  .contact-list li, .practice-info li {
    display: flex; align-items: center; gap: 8px; margin-bottom: 7px;
  }
  .icon { width: 13px; height: 13px; flex: none; }
  .practice-info {
    position: absolute; right: 34px; bottom: 60px;
    list-style: none;
    font-size: 12.5px;
    color: var(--dark-text);
    text-align: right;
  }
  .practice-info li { justify-content: flex-end; }

  /* Back card */
  .card-back {
    left: 470px; top: 496px;
    background: radial-gradient(circle at 50% 55%, var(--teal-light) 0%, var(--teal) 45%, var(--teal-dark) 100%);
  }
  .card-back .brand {
    position: absolute; left: 150px; top: 110px;
  }
  .card-back .brand-dot {
    width: 74px; height: 74px;
    background: transparent;
    border: 4px solid #ffffff;
  }
  .card-back .brand-name { color: #ffffff; font-size: 31px; }
  .back-rule {
    position: absolute; left: 90px; top: 212px;
    width: 440px; height: 1px;
    background: linear-gradient(90deg, transparent, rgba(255,255,255,0.6), transparent);
  }
  .back-url {
    position: absolute; left: 0; right: 0; top: 228px;
    text-align: center;
    color: #ffffff;
    font-size: 15px;
    letter-spacing: 0.5px;
  }
</style>
</head>
<body>

  <section class="card card-front">
    <div class="front-deco" role="img" aria-label="Faint practice emblem decoration"></div>

    <div class="brand">
      <span class="brand-dot"></span>
      <span class="brand-name">Velmora<br>Chirurgie</span>
    </div>
    <div class="front-rule"></div>

    <div class="person">
      <p class="person-name">Priv. Doz. DDr. Corinna Vestaluk</p>
      <p class="person-title">Fachärztin für Allgemein- &amp; Viszeralchirurgie</p>
      <ul class="contact-list">
        <li>
          <svg class="icon" viewBox="0 0 14 14"><rect x="3.5" y="1" width="7" height="12" rx="1.2" fill="none" stroke="var(--teal)" stroke-width="1.3"/></svg>
          XXX-XXX-XXXX
        </li>
        <li>
          <svg class="icon" viewBox="0 0 14 14"><rect x="1" y="3" width="12" height="8" fill="var(--teal)"/><path d="M1 3 L7 8 L13 3" fill="none" stroke="#fff" stroke-width="1"/></svg>
          info@velmorachirurgie.com
        </li>
      </ul>
    </div>

    <ul class="practice-info">
      <li>300-200-9000
        <svg class="icon" viewBox="0 0 14 14"><path d="M3 1.5 L5.5 1.5 L6.5 4.5 L5 5.5 Q6.5 8.5 8.5 9 L9.5 7.5 L12.5 8.5 L12.5 11 Q7 13 3 7 Q1.5 4 3 1.5Z" fill="var(--teal)"/></svg>
      </li>
      <li>00 dummy city, dummy place 0000
        <svg class="icon" viewBox="0 0 14 14"><path d="M7 13 Q2 7 2 5 A5 5 0 0 1 12 5 Q12 7 7 13Z" fill="var(--teal)"/><circle cx="7" cy="5" r="1.8" fill="#fff"/></svg>
      </li>
      <li>www.velmorachirurgie.com
        <svg class="icon" viewBox="0 0 14 14"><circle cx="7" cy="7" r="5.5" fill="none" stroke="var(--teal)" stroke-width="1.2"/><ellipse cx="7" cy="7" rx="2.3" ry="5.5" fill="none" stroke="var(--teal)" stroke-width="1"/><line x1="1.5" y1="7" x2="12.5" y2="7" stroke="var(--teal)" stroke-width="1"/></svg>
      </li>
    </ul>
  </section>

  <section class="card card-back">
    <div class="brand">
      <span class="brand-dot"></span>
      <span class="brand-name">Velmora<br>Chirurgie</span>
    </div>
    <div class="back-rule"></div>
    <p class="back-url">www.velmorachirurgie.com</p>
  </section>

</body>
</html>
```